Label design needed for a new brain focus supplement. Cervalique.com

Hi I’m looking for a quality label design for a my new supplement. The supplement is a nootropic (brain focus booster). I’ll also upload my competitors designs as a reference and to get some ideas.

I was thinking to use a white glossy background with the gold logo in top with some gold graphics added. Along with some focus driven text.

Dimensions for label are 300mm x 105mm Landscape. Please allow a 5mm safe text area.

Target Market(s)

High achieving focus driven People.

Font styles to use
Sans Serif

Colors

Designer to choose colors to be used in the design.

Requirements
Must have
• Good quality design.
Nice to have
• wording to use on label
• EXTREME FOCUS
• Brain food supplement
• High quality
• Premium blend
• Dietary supplement
Should not have
• Bright colourful colours. This is a premium product and label should show this

```html
<!DOCTYPE html>
<html lang="en">
<head>
<meta charset="utf-8">
<title>Cervalique Brain &amp; Focus Label</title>
<link rel="stylesheet" href="https://fonts.googleapis.com/css2?family=Montserrat:wght@400;500;600;800&family=Comfortaa:wght@500&display=swap">
<style>
  :root {
    --canvas: #ffffff;
    --label: #1c1c1d;
    --label-edge: #252526;
    --gold: #d9b25a;
    --gold-light: #f3dc8e;
    --gold-deep: #a57c28;
    --ink: #1a1a1a;
    --white: #f4f4f4;
    --memory: #4aa8e0;
    --focus: #f28c1e;
    --clarity: #5cb848;
  }
  * { margin: 0; padding: 0; box-sizing: border-box; }
  html, body { width: 1200px; height: 1200px; overflow: hidden; background: var(--canvas); }
  .canvas { position: relative; width: 1200px; height: 1200px; }

  /* 300 x 105 mm wrap at 3.8 px/mm */
  .label {
    position: absolute; left: 30px; top: 400px; width: 1140px; height: 399px;
    background: linear-gradient(90deg, var(--label) 0%, var(--label-edge) 50%, var(--label) 100%);
    font-family: "Montserrat", sans-serif;
    overflow: hidden;
  }
  .front {
    position: absolute; left: 50%; top: 0; width: 420px; height: 100%;
    transform: translateX(-50%);
  }
  .brand {
    position: absolute; top: 26px; left: 0; right: 0;
    display: flex; align-items: center; justify-content: center; gap: 10px;
  }
  .brand-dot { width: 20px; height: 20px; border-radius: 50%; background: var(--gold); }
  .brand-name { font-weight: 600; font-size: 56px; color: var(--gold); letter-spacing: 0.5px; line-height: 1; }
  .tagline {
    position: absolute; top: 94px; left: 0; right: 0; text-align: center;
    font-family: "Comfortaa", sans-serif; font-weight: 500; font-size: 24px;
    letter-spacing: 2.5px; color: var(--white); line-height: 1;
  }
  .hero {
    position: absolute; top: 134px; left: 105px; width: 210px; height: 112px;
    border-radius: 40% 40% 45% 45%;
    background: radial-gradient(ellipse at 50% 50%, var(--gold-light) 0%, var(--gold) 45%, var(--gold-deep) 85%);
  }
  .claims {
    position: absolute; top: 270px; left: 40px; width: 340px; height: 64px;
    border: 1px solid rgba(217, 178, 90, 0.55); border-radius: 8px;
  }
  .claims-badge {
    position: absolute; top: -11px; left: 50%; transform: translateX(-50%);
    background: var(--gold-light); color: var(--ink); padding: 2px 10px; border-radius: 10px;
    font-weight: 800; font-size: 12px; letter-spacing: 3px; white-space: nowrap; line-height: 16px;
  }
  .claims-list {
    position: absolute; top: 20px; left: 0; right: 0;
    display: flex; justify-content: center; gap: 14px; list-style: none;
  }
  .claim { display: flex; align-items: center; gap: 6px; font-size: 13px; color: var(--gold); line-height: 1; }
  .claim svg { width: 22px; height: 22px; flex: none; }
  .claims-footer {
    position: absolute; bottom: -8px; left: 50%; transform: translateX(-50%);
    background: var(--label-edge); padding: 0 6px; font-size: 11px; letter-spacing: 1px;
    color: var(--gold); white-space: nowrap; line-height: 14px;
  }
  .count {
    position: absolute; top: 352px; left: 50%; transform: translateX(-50%);
    background: var(--gold-light); color: var(--ink); padding: 3px 14px; border-radius: 9px 9px 0 0;
    font-weight: 800; font-size: 11px; white-space: nowrap; line-height: 15px;
  }
  .band {
    position: absolute; top: 370px; left: 0; right: 0; height: 7px;
    background: linear-gradient(90deg, var(--gold-deep), var(--gold-light) 50%, var(--gold-deep));
  }
</style>
</head>
<body>
<div class="canvas">
  <section class="label">
    <div class="band"></div>
    <div class="front">
      <div class="brand">
        <span class="brand-dot"></span>
        <span class="brand-name">Cervalique</span>
      </div>
      <p class="tagline">Brain &amp; Focus</p>
      <div class="hero" role="img" aria-label="Golden brain with flexing muscular arms"></div>
      <div class="claims">
        <span class="claims-badge">NOOTROPIC</span>
        <ul class="claims-list">
          <li class="claim">
            <svg viewBox="0 0 36 36"><circle cx="18" cy="18" r="17" fill="var(--memory)"/><circle cx="18" cy="16" r="6" fill="none" stroke="#fff" stroke-width="2.4"/><line x1="15" y1="25" x2="21" y2="25" stroke="#fff" stroke-width="2.4"/></svg>
            MEMORY
          </li>
          <li class="claim">
            <svg viewBox="0 0 36 36"><circle cx="18" cy="18" r="17" fill="var(--focus)"/><circle cx="18" cy="18" r="8" fill="none" stroke="#fff" stroke-width="2.4"/><circle cx="18" cy="18" r="2.5" fill="#fff"/></svg>
            FOCUS
          </li>
          <li class="claim">
            <svg viewBox="0 0 36 36"><circle cx="18" cy="18" r="17" fill="var(--clarity)"/><circle cx="18" cy="18" r="8" fill="none" stroke="#fff" stroke-width="2.4"/><line x1="18" y1="13" x2="18" y2="23" stroke="#fff" stroke-width="2.4"/></svg>
            CLARITY
          </li>
        </ul>
        <span class="claims-footer">DIETARY SUPPLEMENT</span>
      </div>
      <span class="count">60 TABLETS</span>
    </div>
  </section>
</div>
</body>
</html>
```